Employment Agency Website Design

We are working with an employment agency in California.

Some sites to use for content/competitors and inspiration:

https://www.dovelanejobs.example/us/en
https://www.perimowork.example
https://www.tamberlinehire.example
https://www.vintrastaff.example/en
https://www.olmirajobs.example
https://www.quarnstaffing.example

Thank you for taking the time to consider designing a website for us. We are web developers based in Stockton, CA, USA. Most of our projects go through the same process. Understanding this process may help you win a project with us. We custom-code all of our websites in-house. We don’t have any requirements as to what tools you use for your design, but we prefer Figma files. For any design that we label as four-stars, we send it to the client for review. The client picks the final design they want us to use. Once we complete this process, we will continue to show additional clients all the four-star sites and purchase them later. Your designs will have multiple chances to sell. For better chances of success, we ask that you follow these guidelines.

IMAGES:
If you use any images or icons in the design, we ask that you have a link to the asset so we can purchase the image/icon. Most of the designs we submit do not have the customer’s images on them unless they have some great images. Be creative; show us the feeling you are trying to portray with your image choices. Use any royalty-free site you choose. We subscribe to Velsor and mainly use their images, but we can purchase images outside of Velsor. PLEASE NOTE: we will not submit designs to clients with watermarks on the images.

FONTS:
We ask that you identify the fonts used in the design. This can be done in a message if you want. We typically use Google Fonts and Velsor Fonts.

CONTENT:
We're always open to different content and ideas. We often submit designs with stock images so the client can see our vision. We typically take pictures after the website launch to use their images with our vision. Lorem Ipsum is fine for paragraphs, but we ask that you write the headers in correct English. We want to be able to show the vision and identify the sections of the website.

INSPIRATION:
We typically add a couple of links in the brief of websites we like to help you get started in your design.

REVISIONS:
We do not often ask for revisions of the designs unless we see something in the design that may not appeal to the client. If there are slight changes that we want to make, we do that in the development process.

FEEDBACK:
We rarely give feedback on designs during the design process. We are working on many website projects and do not have the time to provide feedback. We usually respond if your request is well thought out and asks specific questions, but a note asking “feedback, please” usually goes unanswered.

```html
<!DOCTYPE html>
<html lang="en">
<head>
<meta charset="utf-8">
<title>Corvane — Where the right people meet the right work</title>
<link href="https://fonts.googleapis.com/css2?family=Montserrat:wght@400;500;600;700&family=Arimo:wght@400;700&display=swap" rel="stylesheet">
<style>
:root{
  --red:#c0202e;
  --red-dark:#a51a26;
  --ink:#1e1e1e;
  --text:#333;
  --muted:#555;
  --field:#eeeeee;
  --light:#f2f2f2;
  --footer:#333333;
  --footer-text:#cfcfcf;
  --white:#fff;
}
*{box-sizing:border-box;margin:0;padding:0}
html,body{width:1200px;height:4747px;overflow:hidden;background:var(--white)}
body{font-family:"Arimo",Arial,sans-serif;color:var(--text);position:relative}
.abs{position:absolute}
h1,h2,h3,h4,.mont{font-family:"Montserrat",Arial,sans-serif}
a{color:inherit;text-decoration:none}

.topbar{left:0;top:0;width:1200px;height:52px;background:#111;color:#fff;font-size:15px;display:flex;justify-content:center;align-items:center;gap:18px}
.nav{left:0;top:52px;width:1200px;height:88px;background:#fff}
.brand{left:37px;top:23px;display:flex;align-items:center;gap:10px}
.brand-mark{width:40px;height:40px;border-radius:50%;background:var(--red)}
.brand-name{font-family:"Montserrat",sans-serif;font-weight:600;font-size:30px;color:var(--ink);line-height:1}
.nav-links{left:341px;top:32px;display:flex;gap:34px;font-family:"Montserrat",sans-serif;font-size:16px;color:var(--ink);font-weight:500}
.btn{display:inline-flex;align-items:center;justify-content:center;font-family:"Montserrat",sans-serif;font-weight:700;border-radius:4px}
.btn-outline{left:875px;top:22px;width:122px;height:44px;border:2px solid #555;color:#333;font-size:17px;font-weight:600}
.btn-red{background:var(--red);color:#fff}
.btn-findjob{left:1004px;top:22px;width:161px;height:44px;font-size:17px}

.hero{left:0;top:140px;width:1200px;height:671px;background:linear-gradient(100deg,#4a3c32 0%,#6b5a4b 35%,#a49587 60%,#5b6a76 80%,#3b3b3b 100%)}
.hero h1{position:absolute;left:125px;top:178px;color:#fff;font-size:52px;line-height:54px;font-weight:700}
.btn-request{left:128px;top:376px;width:187px;height:41px;font-size:17px}
.apply{left:337px;top:383px;color:#fff;font-family:"Montserrat",sans-serif;font-weight:700;font-size:18px;text-decoration:underline}
.accent-frame{left:94px;top:760px;width:262px;height:138px;border:4px solid var(--red);border-top:none}
.search{left:110px;top:724px;width:978px;height:157px;background:#fff;box-shadow:0 8px 24px rgba(0,0,0,.12);border-radius:3px}
.search label{position:absolute;top:36px;font-family:"Montserrat",sans-serif;font-weight:600;font-size:16px;color:var(--ink)}
.search .field{position:absolute;top:68px;height:54px;background:var(--field);border-radius:3px;font-size:13px;color:#666;padding:18px 12px}
.btn-search{left:776px;top:68px;width:162px;height:54px;font-size:17px}

.photo{border-radius:2px}
.exp-photo{left:127px;top:1004px;width:489px;height:443px;background:linear-gradient(135deg,#6e5a48,#9c8673 50%,#c9bfb4)}
.red-rule{width:4px;background:var(--red)}
.heading-lg{font-family:"Montserrat",sans-serif;font-weight:500;color:var(--ink);font-size:40px;line-height:46px}
.para{font-size:14px;line-height:20px;color:var(--text)}
.btn-work{left:689px;top:1360px;width:172px;height:48px;font-size:16px}

.how{left:0;top:1511px;width:1200px;height:529px;background:linear-gradient(180deg,var(--red) 0%,var(--red-dark) 100%)}
.how h2{position:absolute;left:0;width:1200px;top:176px;text-align:center;color:#fff;font-size:33px;font-weight:700}
.how p{position:absolute;left:320px;width:560px;top:236px;text-align:center;color:#fff;font-size:14px;line-height:20px}
.step{top:1850px;width:306px;height:292px;background:#fff;box-shadow:0 6px 20px rgba(0,0,0,.12);text-align:center}
.step svg{position:absolute;left:105px;top:34px}
.step h3{position:absolute;left:20px;right:20px;top:164px;font-size:16px;font-weight:600;color:#333;line-height:19px}
.step p{position:absolute;left:30px;right:30px;top:214px;font-size:14px;line-height:19px;color:#555}

.fields-title{left:0;width:1200px;top:2252px;text-align:center;font-family:"Montserrat",sans-serif;font-weight:600;font-size:33px;color:var(--ink)}
.tile{top:2344px;width:222px;height:301px;border-radius:3px;overflow:hidden}
.tile span{position:absolute;left:0;right:0;bottom:24px;text-align:center;color:#fff;font-family:"Montserrat",sans-serif;font-weight:700;font-size:21px}

.talent{left:0;top:2746px;width:1200px;height:562px;background:var(--light)}
.talent-photo{left:535px;top:0;width:665px;height:562px;background:linear-gradient(90deg,#eeeeee 0%,#c8a890 30%,#a8572c 60%,#6f8aa6 85%,#dcdcdc 100%)}

.career-photo{left:0;top:3360px;width:606px;height:433px;background:linear-gradient(120deg,#3c5a48 0%,#7a6a58 45%,#cfc7bd 75%,#8a8a8a 100%)}

.insights-title{left:0;width:1200px;top:3892px;text-align:center;font-family:"Montserrat",sans-serif;font-weight:500;font-size:38px;color:var(--ink)}
.post{top:3968px;width:299px}
.post .thumb{width:299px;height:195px;border-radius:2px}
.post .date{margin-top:28px;font-family:"Montserrat",sans-serif;font-size:16px;color:#888;font-weight:500}
.post h4{margin-top:12px;font-size:20px;line-height:26px;font-weight:500;color:var(--ink)}

.footer{left:0;top:4364px;width:1200px;height:383px;background:var(--footer);color:var(--footer-text)}
.footer .divider{position:absolute;top:0;width:1px;height:293px;background:#5a5a5a}
.footer h5{font-family:"Montserrat",sans-serif;font-weight:700;color:#fff;font-size:19px;margin-bottom:16px}
.footer .col{position:absolute;top:60px;font-size:13.5px;line-height:21px}
.footer ul{list-style:none}
.footer li{line-height:28px;font-size:14px}
.foot-brand{left:115px;top:92px;width:212px;text-align:center}
.foot-brand .mark{width:86px;height:86px;border-radius:50%;background:var(--red);margin:0 auto 14px}
.foot-brand .name{font-family:"Montserrat",sans-serif;font-weight:600;font-size:30px;color:#fff}
.foot-rule{left:127px;top:293px;width:946px;height:1px;background:#5a5a5a}
.copy{left:130px;top:320px;font-size:13px}
.social{left:993px;top:322px;display:flex;gap:14px}
.social span{width:12px;height:12px;border-radius:50%;background:#ddd}
</style>
</head>
<body>

<div class="abs topbar"><span>Are you a job seeker?</span><span>|</span><span>Are you an employer?</span></div>

<header class="abs nav">
  <div class="abs brand"><span class="brand-mark"></span><span class="brand-name">Corvane</span></div>
  <nav class="abs nav-links"><a>Job Seekers</a><a>Employers</a><a>Why Us?</a><a>Blog</a><a>About us</a></nav>
  <a class="abs btn btn-outline">Login</a>
  <a class="abs btn btn-red btn-findjob">Find a Job</a>
</header>

<section class="abs hero" role="img" aria-label="Photo of a smiling woman with curly hair working on a laptop in a bright office">
  <h1>Where the right<br>people meet the<br>right work.</h1>
  <a class="abs btn btn-red btn-request">Request Talent</a>
  <a class="abs apply">Apply Job</a>
</section>

<div class="abs accent-frame"></div>
<form class="abs search">
  <label style="left:42px">Keyword</label>
  <div class="field" style="left:42px;width:352px">Job Title, Industry, Keywords</div>
  <label style="left:410px">Location</label>
  <div class="field" style="left:410px;width:352px">Location or Zip Code</div>
  <a class="abs btn btn-red btn-search">Search Jobs</a>
</form>

<div class="abs photo exp-photo" role="img" aria-label="Photo of a team of colleagues collaborating around laptops at a shared desk"></div>
<div class="abs red-rule" style="left:663px;top:1027px;height:147px"></div>
<h2 class="abs heading-lg" style="left:688px;top:1013px;width:420px">Bringing expertise together with real partnership.</h2>
<p class="abs para" style="left:690px;top:1178px;width:386px">Lorem ipsum dolor sit amet, consectetur adipiscing elit, sed do eiusmod tempor incididunt ut labore et dolore magna aliqua. Quis ipsum suspendisse ultrices gravida. Risus commodo viverra maecenas accumsan.Lorem ipsum dolor sit amet, consectetur adipiscing elit, sed do eiusmod tempor incididunt ut labore et dolore magna aliqua. Quis ipsum suspendisse ultrices gravida. Risus commodo viverrmsan lacus vel facilisis.</p>
<a class="abs btn btn-red btn-work">Work With Us</a>

<section class="abs how">
  <svg class="abs" style="left:0;top:0" width="1200" height="160" viewBox="0 0 1200 160">
    <polygon points="0,0 1200,0 600,110" fill="#fff"/>
    <polyline points="0,10 600,128 1200,10" fill="none" stroke="#fff" stroke-width="5"/>
  </svg>
  <h2>How It Works</h2>
  <p>Lorem ipsum dolor sit amet, consectetur adipiscing elit, sed do eiusmod tempor incididunt ut labore et dolore magna aliqua. Quis ipsum suspendisse ultrices gravida. Risus commodo viverra maecenas accumsan.</p>
</section>

<div class="abs step" style="left:127px">
  <svg width="96" height="110" viewBox="0 0 96 110"><polygon points="48,4 92,29 92,81 48,106 4,81 4,29" fill="none" stroke="#c0202e" stroke-width="5"/>
    <rect x="32" y="34" width="32" height="40" fill="none" stroke="#333" stroke-width="2"/><line x1="38" y1="44" x2="58" y2="44" stroke="#333" stroke-width="2"/><line x1="38" y1="52" x2="58" y2="52" stroke="#333" stroke-width="2"/><line x1="38" y1="60" x2="58" y2="60" stroke="#333" stroke-width="2"/><line x1="38" y1="67" x2="50" y2="67" stroke="#333" stroke-width="2"/></svg>
  <h3>1. Describe &nbsp;your need</h3>
  <p>Lorem ipsum dolor sit amet, conse ctetur adipiscing elit, sed do.</p>
</div>
<div class="abs step" style="left:448px">
  <svg width="96" height="110" viewBox="0 0 96 110"><polygon points="48,4 92,29 92,81 48,106 4,81 4,29" fill="none" stroke="#c0202e" stroke-width="5"/>
    <circle cx="48" cy="46" r="7" fill="none" stroke="#333" stroke-width="2"/><circle cx="33" cy="50" r="5" fill="none" stroke="#333" stroke-width="2"/><circle cx="63" cy="50" r="5" fill="none" stroke="#333" stroke-width="2"/><path d="M36 70 Q48 52 60 70 Z" fill="none" stroke="#333" stroke-width="2"/><path d="M24 68 Q33 56 40 64" fill="none" stroke="#333" stroke-width="2"/><path d="M56 64 Q63 56 72 68" fill="none" stroke="#333" stroke-width="2"/></svg>
  <h3>2. View matching<br>candidates</h3>
  <p>Lorem ipsum dolor sit amet, conse ctetur adipiscing elit, sed do.</p>
</div>
<div class="abs step" style="left:767px">
  <svg width="96" height="110" viewBox="0 0 96 110"><polygon points="48,4 92,29 92,81 48,106 4,81 4,29" fill="none" stroke="#c0202e" stroke-width="5"/>
    <circle cx="48" cy="40" r="7" fill="none" stroke="#333" stroke-width="2"/><circle cx="33" cy="66" r="7" fill="none" stroke="#333" stroke-width="2"/><circle cx="63" cy="66" r="7" fill="none" stroke="#333" stroke-width="2"/><line x1="44" y1="47" x2="37" y2="59" stroke="#333" stroke-width="2"/><line x1="52" y1="47" x2="59" y2="59" stroke="#333" stroke-width="2"/><line x1="40" y1="66" x2="56" y2="66" stroke="#333" stroke-width="2"/></svg>
  <h3>3. Connect with a recruiter<br>to consult and hire</h3>
  <p>Lorem ipsum dolor sit amet, conse ctetur adipiscing elit, sed do.</p>
</div>

<h2 class="abs fields-title">Fluent in your fields and industries.</h2>
<div class="abs tile" style="left:127px;background:linear-gradient(180deg,#b59a80,#5a5048)" role="img" aria-label="Photo of a calculator and paperwork on a desk"><span>Accounting</span></div>
<div class="abs tile" style="left:368px;background:linear-gradient(180deg,#9a7a4a,#3e3226)" role="img" aria-label="Photo of a professional reviewing documents"><span>Government</span></div>
<div class="abs tile" style="left:610px;background:linear-gradient(180deg,#c9c6c0,#4e4a48)" role="img" aria-label="Photo of a group of students studying together"><span>Education</span></div>
<div class="abs tile" style="left:850px;background:linear-gradient(180deg,#7c6a5a,#2d3440)" role="img" aria-label="Photo of an engineer working on a laptop in a workshop"><span>Engineering</span></div>

<section class="abs talent">
  <div class="abs talent-photo" role="img" aria-label="Photo of a smiling man leaning over a colleague working on a laptop"></div>
  <div class="abs red-rule" style="left:105px;top:166px;height:147px"></div>
  <h2 class="abs heading-lg" style="left:131px;top:155px;width:420px">Find talent to get<br>more done</h2>
  <p class="abs para" style="left:131px;top:258px;width:385px">Lorem ipsum dolor sit amet, consectetur adipiscing elit, sed do eiusmod tempor incididunt ut labore et dolore magna aliqua. Quis ipsum suspendisse ultrices gravida. Risus commodo viverra maecenas accumsan.</p>
  <p class="abs para" style="left:131px;top:358px;width:385px">Lorem ipsum dolor sit amet, consectetur adipiscing elit, sed do eiusmod tempor incididunt ut labore et dolore magna aliqua. Quis ipsum suspendisse ultrices gravida. Risus commodo viverrmsan lacus vel facilisis.</p>
</section>

<div class="abs career-photo" role="img" aria-label="Photo of a smiling woman typing on a laptop beside a coffee cup"></div>
<div class="abs red-rule" style="left:662px;top:3450px;height:147px"></div>
<h2 class="abs heading-lg" style="left:686px;top:3436px;width:420px">Make the career<br>move you want</h2>
<p class="abs para" style="left:686px;top:3542px;width:385px">Lorem ipsum dolor sit amet, consectetur adipiscing elit, sed do eiusmod tempor incididunt ut labore et dolore magna aliqua. Quis ipsum suspendisse ultrices gravida. Risus commodo viverra maecenas accumsan.</p>
<p class="abs para" style="left:686px;top:3642px;width:385px">Lorem ipsum dolor sit amet, consectetur adipiscing elit, sed do eiusmod tempor incididunt ut labore et dolore magna aliqua. Quis ipsum suspendisse ultrices gravida. Risus commodo viverrmsan lacus vel facilisis.</p>

<h2 class="abs insights-title">Discover more insights</h2>
<article class="abs post" style="left:127px"><div class="thumb" style="background:linear-gradient(135deg,#3f6f8f,#a7b8c4)" role="img" aria-label="Photo of two colleagues discussing work at a laptop"></div><div class="date">February 29, 2024</div><h4 class="mont">Lorem ipsum dolor sit am consectetur adipiscin</h4></article>
<article class="abs post" style="left:452px"><div class="thumb" style="background:linear-gradient(135deg,#2f3a44,#b06a44 55%,#d8d2cc)" role="img" aria-label="Photo of a woman working on a laptop in an office"></div><div class="date">February 29, 2024</div><h4 class="mont">Lorem ipsum dolor sit am consectetur adipiscin</h4></article>
<article class="abs post" style="left:774px"><div class="thumb" style="background:linear-gradient(135deg,#6f7a5c,#c7b9a6 55%,#8a8f96)" role="img" aria-label="Photo of a team meeting around a table with laptops"></div><div class="date">February 29, 2024</div><h4 class="mont">Lorem ipsum dolor sit am consectetur adipiscin</h4></article>

<footer class="abs footer">
  <div class="divider" style="left:356px"></div>
  <div class="divider" style="left:658px"></div>
  <div class="divider" style="left:907px"></div>
  <div class="abs foot-brand"><div class="mark"></div><div class="name">Corvane</div></div>
  <div class="col" style="left:391px;width:230px"><h5>ABOUT US</h5><p>Lorem ipsum dolor sit amet, con sectetur adipiscing elit, sed lo do eiusmod tempor incididunt ut labore et dolore magna aliquauis ipsum suspendisse ultlorerices gravidaisus commodo.</p></div>
  <div class="col" style="left:701px"><h5>EXPERTISE</h5><ul><li>Accounting &amp; Finance</li><li>Administrative &amp; Office</li><li>Contact Center</li><li>Education</li><li>Engineering</li><li>Government</li></ul></div>
  <div class="col" style="left:950px"><h5>LINKS</h5><ul><li>Find a Job</li><li>Careers</li><li>Employee Login</li><li>Employee Support</li></ul></div>
  <div class="abs foot-rule"></div>
  <div class="abs copy">© Copyright 2024 All Rights Are Reserved.</div>
  <div class="abs social" aria-label="Social links"><span></span><span></span><span></span></div>
</footer>

</body>
</html>
```